Express envelope design for courier company

We're a courier company launching a new service for sending documents around Australia. We need a design for the express envelope that will be used to hold the documents during transit. The envelope will be printed in colour on cardboard. Please see brief attached.

Design cues:
• Vibrant
• Simplified
• Clean
• Aesthetically pleasing
• Artistic
• Nothing “institutional” or “Harwick Lines”
• Nothing cramped, no small text

It's fine to crop, recolour, or reinterpret the logo.

Industry/Entity Type

It Company

Font styles to use
Sans Serif

Requirements
Must have
• Dimensions:
• Back side: 350 x 230 mm
• Front side: 387.5 x 230 mm (including flap to close envelope)
• Back side barcode panel: 90 x 75 mm (blank area for adhesive barcode)
• Back side address panel: 150 x 90 mm (see PDF for contents and layout)
• Front side text:
• QM-DR
• Express Envelope
• Send With Trust
• 1300 584 961
• qmdr.com.au
• Back side text:
• For documents
• Max. weight 500g, max width 20mm
• Send With Trust
• • Time-guaranteed and next-flight-out service for vital deliveries
• • Same-day and next-day local services
• • Overnight service to most Australian locations
• • Budget road service Australia-wide
• • Worldwide express courier
• Visit qmdr.com.au or phone 1300 584 961
• Flap text:
• Go to qmdr.com.au to book your pickup.
• Carried subject to QM-DR Standard Conditions of Carriage; see our website.
Nice to have
• Our web colours:
• #fcd614
• #d06517
• #3b5274
• #f0f0d8
• #382a3a

```html
<!DOCTYPE html>
<html lang="en">
<head>
<meta charset="utf-8">
<title>QM-DR Express Envelope</title>
<link href="https://fonts.googleapis.com/css2?family=Archivo:ital,wght@0,800;1,800&family=Roboto+Condensed:ital,wght@0,400;0,700;1,700&display=swap" rel="stylesheet">
<style>
  :root {
    --yellow: #fcd614;
    --orange: #d06517;
    --navy: #3b5274;
    --cream: #f0f0d8;
    --ink: #382a3a;
    --backdrop: #94b3bd;
    --white: #ffffff;
  }
  * { margin: 0; padding: 0; box-sizing: border-box; }
  html, body { width: 960px; height: 1200px; overflow: hidden; }
  body {
    background: var(--backdrop);
    font-family: "Roboto Condensed", Arial, sans-serif;
    position: relative;
  }

  /* ---------- Front face ---------- */
  .envelope-front {
    position: absolute;
    left: 85px; top: 26px;
    width: 744px; height: 506px;
    background: var(--navy);
    transform: rotate(-4.1deg);
    overflow: hidden;
  }
  .pinstripe { position: absolute; left: 0; width: 100%; background: var(--yellow); }
  .pinstripe.one { top: 64px; height: 4px; }
  .pinstripe.two { top: 79px; height: 3px; }
  .pinstripe.three { top: 92px; height: 5px; }

  .brand-name {
    position: absolute;
    left: 0; top: 22px; width: 100%;
    text-align: center;
    font-family: "Roboto Condensed", Arial, sans-serif;
    font-weight: 700; font-size: 30px; line-height: 36px;
    color: var(--yellow);
  }

  .title-band {
    position: absolute; left: 0; top: 154px;
    width: 100%; height: 134px;
    background: var(--orange);
  }
  .title-band .fill {
    position: absolute; left: 0; top: 17px; width: 100%; height: 100px;
    background: var(--yellow);
  }
  .title {
    position: absolute; left: 42px; top: 20px;
    font-family: "Archivo", Arial, sans-serif;
    font-style: italic; font-weight: 800;
    font-size: 74px; line-height: 1;
    color: var(--navy); letter-spacing: 0.5px;
  }

  .front-contact {
    position: absolute; right: 108px; top: 322px;
    text-align: right;
    font-weight: 700; font-style: italic;
    font-size: 25px; line-height: 30px;
    color: var(--white);
  }
  .front-slogan {
    position: absolute; right: 108px; top: 386px;
    font-weight: 700; font-style: italic;
    font-size: 51px; line-height: 1;
    color: var(--yellow);
  }
  .base-band {
    position: absolute; left: 0; top: 452px;
    width: 100%; height: 34px;
    background: var(--orange);
  }
  .base-band .fill {
    position: absolute; left: 0; top: 8px; width: 100%; height: 18px;
    background: var(--yellow);
  }

  /* ---------- Back face ---------- */
  .envelope-back {
    position: absolute;
    left: 88px; top: 583px;
    width: 759px; height: 516px;
    transform: rotate(2.7deg);
  }
  .back-body {
    position: absolute; left: 0; top: 0;
    width: 690px; height: 516px;
    background: var(--navy);
    overflow: hidden;
  }
  .barcode-panel {
    position: absolute; left: 12px; top: 20px;
    width: 197px; height: 170px;
    background: var(--cream);
    border: 2px solid var(--ink);
  }
  .back-slogan {
    position: absolute; left: 278px; top: 34px;
    font-weight: 700; font-style: italic;
    font-size: 52px; line-height: 1;
    color: var(--yellow);
  }
  .service-list {
    position: absolute; left: 276px; top: 90px;
    list-style: none;
    font-size: 14.5px; line-height: 17.5px;
    color: var(--white);
  }
  .service-list li::before { content: "\2022\00a0"; }

  .visit-band {
    position: absolute; left: 0; top: 196px;
    width: 100%; height: 41px;
    background: var(--orange);
  }
  .visit-band .fill {
    position: absolute; left: 0; top: 6px; width: 100%; height: 28px;
    background: var(--yellow);
    display: flex; align-items: center; justify-content: center;
    padding-left: 190px;
    font-size: 21px; color: var(--navy);
  }

  .lower-band {
    position: absolute; left: 0; top: 418px;
    width: 100%; height: 38px;
    background: var(--orange);
  }
  .lower-band .fill {
    position: absolute; left: 0; top: 9px; width: 100%; height: 20px;
    background: var(--yellow);
  }

  .address-panel {
    position: absolute; left: 9px; top: 270px;
    width: 332px; height: 214px;
    background: var(--cream);
    border: 1px solid var(--ink);
    color: var(--navy);
    font-size: 10px;
  }
  .address-row { position: absolute; left: 0; width: 100%; border-bottom: 2px solid var(--navy); }
  .address-row.sender { top: 0; height: 28px; }
  .address-label { position: absolute; left: 12px; }
  .address-row.sender .address-label { top: 8px; }
  .receiver-label { top: 40px; }
  .address-footer {
    position: absolute; left: 0; bottom: 0; width: 100%; height: 44px;
    border-top: 2px solid var(--navy);
  }
  .address-footer .divider {
    position: absolute; left: 158px; top: 0; bottom: 0;
    border-left: 2px solid var(--navy);
  }
  .address-footer .state { left: 12px; top: 6px; }
  .address-footer .postcode { left: 170px; top: 12px; }

  .limits {
    position: absolute; left: 357px; top: 280px;
    color: var(--white);
  }
  .limits h2 {
    font-family: "Archivo", Arial, sans-serif;
    font-style: normal; font-weight: 800;
    font-size: 23px; line-height: 1;
    color: var(--yellow); margin-bottom: 12px;
  }
  .limits p { font-size: 30px; line-height: 40px; }

  .flap {
    position: absolute; left: 660px; top: 10px;
    width: 99px; height: 500px;
  }
  .flap svg { position: absolute; left: 0; top: 0; }
  .flap-text {
    position: absolute; left: 52px; top: 60px;
    transform-origin: 0 0;
    transform: rotate(90deg);
    width: 380px;
    font-size: 10.5px; line-height: 13px;
    color: var(--white);
    white-space: nowrap;
  }
</style>
</head>
<body>

<section class="envelope-front" aria-label="Envelope front">
  <div class="pinstripe one"></div>
  <div class="pinstripe two"></div>
  <div class="pinstripe three"></div>

  <p class="brand-name">QM-DR</p>

  <div class="title-band">
    <div class="fill"></div>
    <h1 class="title">Express Envelope</h1>
  </div>

  <p class="front-contact">1300 584 961<br>qmdr.com.au</p>
  <p class="front-slogan">Ship With Trust</p>

  <div class="base-band"><div class="fill"></div></div>
</section>

<section class="envelope-back" aria-label="Envelope back">
  <div class="back-body">
    <div class="barcode-panel" aria-label="Space for barcode label"></div>

    <p class="back-slogan">Ship With Trust</p>
    <ul class="service-list">
      <li>Time-guaranteed and next-flight-out service for vital deliveries</li>
      <li>Same-day and next-day local services</li>
      <li>Overnight service to most Australian locations</li>
      <li>Budget road service Australia-wide</li>
      <li>Worldwide express courier</li>
    </ul>

    <div class="visit-band">
      <div class="fill">Visit qmdr.com.au or phone 1300 584 961</div>
    </div>

    <div class="lower-band"><div class="fill"></div></div>

    <div class="address-panel">
      <div class="address-row sender"><span class="address-label">Sender's Name</span></div>
      <span class="address-label receiver-label">Receiver</span>
      <div class="address-footer">
        <span class="address-label state">State</span>
        <span class="divider"></span>
        <span class="address-label postcode">Postcode</span>
      </div>
    </div>

    <div class="limits">
      <h2>For Documents</h2>
      <p>Max. weight 500g</p>
      <p>Max width 20mm</p>
    </div>
  </div>

  <div class="flap">
    <svg width="99" height="500" viewBox="0 0 99 500" aria-hidden="true">
      <path d="M30 2 H97 V498 L40 480 C20 476 8 470 8 455 V28 C8 12 16 3 30 2 Z"
            fill="var(--navy)" stroke="var(--ink)" stroke-width="2"/>
    </svg>
    <p class="flap-text">Go to qmdr.com.au to book your pickup.<br>Carried subject to QM-DR Standard Conditions of Carriage; see our website.</p>
  </div>
</section>

</body>
</html>
```